A new fresh and flat K&T Logistics Brochure Design A4 - 4 pages

Our client is an established International Logistics firm looking to upgrade their sales brochure.
We would like the designer to create concepts that are flat, modern and communicate reliability and expediency to our clients. We want the brochure to maintain a degree of white space and minimal design.
Introduction
LOGISTICS - it's what we do best! We're proud to say so after 27 years (and counting) of organic growth within the 3PL industry. Starting off in Meridian, Mississippi with a fleet of 4 trucks in 1987, K&T is today a global 3PL company with offices in the United States and Asia Pacific region.
Our goal has always been to serve our clients by getting things done, and getting them done right.
Format: A4 4-sided brochure
Pg 1 Front Page - Company name and logo, and vector design concept to make front page unique. Please try to include some kind of container reference design on the front page (e.g 2D or 3D vector, transparent overlay etc...), place this design element somewhere in the middle or bttom of the page.
Pg 2 and/or Pg 3
- Introduction and Core services Including: ABOUT, SERVICES, CONTRACT LOGISTICS, K&T INTEL (following the menu content of our website www.ktvrx.example)
- Text space to explain Services in more detail.
Social proof (existing client testimonials/feedback.)
- A 'C.A.R.E' acronym design element, including the words: Communicative, Accessible, Responsible, Efficient
Pg 4 Back Page- Contact information, Call to action.
Throughut the brochure please leave space for images as you deem appropriate and we will update late OR even better usesome of your own stock images.
Color theme: Based on corporate colors (but not limited to), see website
http://www.ktvrx.example
Try diffent font types to the website both serif and sans serif
Include several CTAs throughout the brochure.
You can use both the attached pdf brochure and the website for content.
We would also appreciate if you could also enhance the logo to make it 'pop' (keep shape and style).

```html
<!DOCTYPE html>
<html lang="en">
<head>
<meta charset="utf-8">
<title>K&amp;T Logistics – Company Introduction</title>
<link href="https://fonts.googleapis.com/css2?family=Arimo:wght@400;700&family=Lato:wght@300;700&display=swap" rel="stylesheet">
<style>
  :root {
    --page-bg: #ffffff;
    --panel-grey: #e4e5e7;
    --band-slate: #4a6579;
    --band-line: #8fa3b2;
    --brand-blue: #1f6c95;
    --brand-slate: #3d5a70;
    --text-light: #ffffff;
    --watermark: rgba(40, 60, 80, 0.08);
  }
  * { box-sizing: border-box; margin: 0; padding: 0; }
  html, body { width: 1200px; height: 1000px; overflow: hidden; background: var(--page-bg); }
  .spread {
    position: absolute; left: 58px; top: 123px;
    width: 1077px; height: 761px;
    background: var(--panel-grey);
    overflow: hidden;
  }
  .back-cover { position: absolute; left: 0; top: 0; width: 538px; height: 605px; background: var(--panel-grey); }
  .front-cover { position: absolute; left: 538px; top: 0; width: 539px; height: 605px;
    background: linear-gradient(180deg, #f4f4f5 0%, #ffffff 30%); }
  .brand { position: absolute; left: 44px; top: 40px; display: flex; align-items: flex-end; gap: 14px; }
  .brand-mark { display: flex; align-items: center; gap: 10px; }
  .brand-square { width: 18px; height: 18px; background: var(--brand-blue); }
  .brand-name { font-family: "Arimo", Arial, sans-serif; font-weight: 700; font-size: 58px; line-height: 1; color: var(--brand-blue); }
  .brand-tagline { font-family: "Arimo", Arial, sans-serif; font-weight: 700; font-size: 17px; color: var(--brand-slate); padding-bottom: 2px; }
  .photo-grid {
    position: absolute; left: 18px; top: 138px;
    display: grid; grid-template-columns: repeat(4, 123px); grid-template-rows: repeat(4, 110px);
    column-gap: 3.7px; row-gap: 4px;
  }
  .photo-tile { border-radius: 8px; }
  .t1 { background: linear-gradient(160deg, #c9ccce, #8c9094); }
  .t2 { background: linear-gradient(160deg, #d9d4cf, #b3282d); }
  .t3 { background: linear-gradient(180deg, #a9c2d6, #4d6f8f 55%, #9b4a3c); }
  .t4 { background: linear-gradient(180deg, #b0c7d8, #5d7d98 50%, #a6463a); }
  .t5 { background: linear-gradient(160deg, #e6e8ea, #8a8a86); }
  .t6 { background: linear-gradient(160deg, #c7dcea, #e3902c 60%, #c24a2e); }
  .t7 { background: linear-gradient(180deg, #5d7890, #9c4535); }
  .t8 { background: linear-gradient(180deg, #6b5a4e, #a24a3d 60%, #c9b36a); }
  .t9 { background: linear-gradient(180deg, #e3e6e9, #6c6f72); }
  .t10 { background: linear-gradient(180deg, #dfe3e6, #7b7c7b); }
  .t11 { background: linear-gradient(160deg, #e58a2c, #4b6e8e 60%, #5a6a74); }
  .t12 { background: linear-gradient(160deg, #f08c2a, #3f5d7c 60%, #7c8a92); }
  .t13 { background: linear-gradient(160deg, #b3342a, #d6d2c4 60%, #a5352d); }
  .t14 { background: linear-gradient(160deg, #2e5fa3, #3f7d5a 55%, #d1cfc6); }
  .t15 { background: linear-gradient(160deg, #8e7e6c, #2f6fa4 55%, #8b8e90); }
  .t16 { background: linear-gradient(160deg, #e67c27, #8a8f92 55%, #6d6f70); }
  .info-band {
    position: absolute; left: 0; top: 605px; width: 1077px; height: 156px;
    background: var(--band-slate);
  }
  .info-band::before { content: ""; position: absolute; left: 0; right: 0; top: 5px; height: 1px; background: var(--band-line); }
  .back-watermark {
    position: absolute; left: 40px; top: 425px; z-index: 1;
    font-family: "Arimo", Arial, sans-serif; font-weight: 700; font-size: 260px; line-height: 1;
    color: var(--watermark); pointer-events: none; white-space: nowrap;
  }
  .contact-list { position: absolute; left: 310px; top: 19px; list-style: none; z-index: 2;
    font-family: "Arimo", Arial, sans-serif; font-size: 12.5px; color: var(--text-light); line-height: 18px; }
  .contact-item { display: flex; align-items: flex-start; gap: 8px; margin-bottom: 7px; }
  .contact-icon { width: 26px; height: 26px; flex: none; }
  .cover-title { position: absolute; right: 28px; top: 17px; text-align: right; z-index: 2;
    font-family: "Lato", sans-serif; color: var(--text-light); line-height: 1; }
  .cover-title-light { display: block; font-weight: 300; font-size: 42px; letter-spacing: 0.5px; }
  .cover-title-bold { display: block; font-weight: 700; font-size: 42px; margin-top: 8px; }
</style>
</head>
<body>
  <div class="spread">
    <section class="back-cover" aria-label="Back cover"></section>

    <section class="front-cover">
      <div class="brand">
        <div class="brand-mark">
          <span class="brand-square"></span>
          <span class="brand-name">K&amp;T</span>
        </div>
        <span class="brand-tagline">Logistics and Supply Chain Solutions</span>
      </div>

      <div class="photo-grid">
        <div class="photo-tile t1" role="img" aria-label="Photo: trucks carrying white shipping containers"></div>
        <div class="photo-tile t2" role="img" aria-label="Photo: container crane stairway above trucks"></div>
        <div class="photo-tile t3" role="img" aria-label="Photo: container ship at sea"></div>
        <div class="photo-tile t4" role="img" aria-label="Photo: container ship deck and ocean"></div>
        <div class="photo-tile t5" role="img" aria-label="Photo: open cargo aircraft nose"></div>
        <div class="photo-tile t6" role="img" aria-label="Photo: containers being lifted by crane"></div>
        <div class="photo-tile t7" role="img" aria-label="Photo: stacked containers on a ship"></div>
        <div class="photo-tile t8" role="img" aria-label="Photo: container stacks on a vessel"></div>
        <div class="photo-tile t9" role="img" aria-label="Photo: air cargo being loaded onto aircraft"></div>
        <div class="photo-tile t10" role="img" aria-label="Photo: ground crew beside cargo aircraft"></div>
        <div class="photo-tile t11" role="img" aria-label="Photo: straddle carrier in container yard"></div>
        <div class="photo-tile t12" role="img" aria-label="Photo: straddle carriers moving containers"></div>
        <div class="photo-tile t13" role="img" aria-label="Photo: stacked red and white containers"></div>
        <div class="photo-tile t14" role="img" aria-label="Photo: blue and green containers in port"></div>
        <div class="photo-tile t15" role="img" aria-label="Photo: container yard from above"></div>
        <div class="photo-tile t16" role="img" aria-label="Photo: straddle carrier on wet quay"></div>
      </div>
    </section>

    <footer class="info-band">
      <ul class="contact-list">
        <li class="contact-item">
          <svg class="contact-icon" viewBox="0 0 26 26" aria-hidden="true">
            <rect x="5" y="1" width="17" height="24" rx="2" fill="#fff"/>
            <rect x="1" y="3" width="4" height="20" rx="2" fill="#fff"/>
            <g fill="#4a6579">
              <rect x="9" y="5" width="3" height="3"/><rect x="13" y="5" width="3" height="3"/><rect x="17" y="5" width="3" height="3"/>
              <rect x="9" y="10" width="3" height="3"/><rect x="13" y="10" width="3" height="3"/><rect x="17" y="10" width="3" height="3"/>
              <rect x="9" y="15" width="3" height="3"/><rect x="13" y="15" width="3" height="3"/><rect x="17" y="15" width="3" height="3"/>
            </g>
          </svg>
          <span>+1 (555) 010 2040 (US)<br>+86 (755) 0100 2233 (Asia)<br>+852 5550 1234 (HK)</span>
        </li>
        <li class="contact-item">
          <svg class="contact-icon" viewBox="0 0 26 26" aria-hidden="true">
            <path d="M1 10 L13 2 L25 10 V24 H1 Z" fill="#fff"/>
            <path d="M1 10 L13 18 L25 10" fill="none" stroke="#4a6579" stroke-width="1.5"/>
          </svg>
          <span>info@kttransport.example</span>
        </li>
        <li class="contact-item">
          <svg class="contact-icon" viewBox="0 0 26 26" aria-hidden="true">
            <circle cx="13" cy="13" r="12" fill="#fff"/>
            <path d="M7 6 C10 8 9 11 12 12 C14 13 12 16 10 18 C8 17 6 14 5 12 Z M16 4 C18 6 20 7 21 10 C19 11 17 9 15 8 Z M15 15 C18 14 21 15 20 19 C18 21 16 21 15 18 Z" fill="#4a6579"/>
          </svg>
          <span>www.ktvrx.example</span>
        </li>
      </ul>

      <h1 class="cover-title">
        <span class="cover-title-light">COMPANY</span>
        <span class="cover-title-bold">INTRODUCTION</span>
      </h1>
    </footer>

    <div class="back-watermark" aria-hidden="true">K&amp;T</div>
  </div>
</body>
</html>
```